Generic Business Card

I need a business card for my new cafe which is only six weeks old. I'm continuously asked for a business so that customers can either keep or pass on to a friend. I'd also like a card that I can give out with each bill which contains the business name, address, contact details and website.
The cafe's internal design has an industrial feel to it with modern subdued colours. I have attached an internal photo along with my main hero shot and logo.
The hero shot features prominently on my website and other print material and I would also like it to appear on my bus card.

Target Market(s)

Men & women between 35 and 45 years of age who know and enjoy good coffee.

Industry/Entity Type

Industrial

Contact Information for Business Card

Shop 7b/118-120 Pelbourne Street, East Dalvington 3981
Tel. 9462 3157
www.talvemo.com.au

```html
<!DOCTYPE html>
<html lang="en">
<head>
<meta charset="utf-8">
<title>Talvemo – Business Card</title>
<link rel="stylesheet" href="https://fonts.googleapis.com/css2?family=Tinos:wght@400;700&display=swap">
<style>
  :root {
    --page: #e9e7e4;
    --card-white: #ffffff;
    --ink: #1b1b1b;
    --band-dark: #232323;
    --photo-deep: #121212;
    --photo-dark: #2b2b2b;
    --photo-mid: #5c5c5c;
    --photo-light: #9a9a9a;
    --photo-pale: #d6d6d6;
  }
  * { margin: 0; padding: 0; box-sizing: border-box; }
  html, body {
    width: 1200px;
    height: 750px;
    overflow: hidden;
    background: var(--page);
  }
  .business-card {
    position: relative;
    width: 1200px;
    height: 750px;
    background: var(--card-white);
    overflow: hidden;
    font-family: "Tinos", "Times New Roman", serif;
    color: var(--ink);
  }
  .hero-photo {
    position: absolute;
    left: 0;
    top: 0;
    width: 1200px;
    height: 440px;
    background:
      linear-gradient(to top, rgba(214,214,214,0.95) 0%, rgba(214,214,214,0.75) 14%, rgba(214,214,214,0) 34%),
      linear-gradient(90deg, var(--photo-light) 0%, var(--photo-mid) 14%, var(--photo-dark) 30%, var(--photo-mid) 44%, var(--photo-dark) 58%, var(--photo-deep) 74%, var(--photo-dark) 100%);
  }
  .contact-block {
    position: absolute;
    right: 58px;
    top: 338px;
    text-align: right;
    font-style: normal;
    font-weight: 400;
    font-size: 38px;
    line-height: 50px;
  }
  .contact-block p { white-space: nowrap; }
  .brand {
    position: absolute;
    left: 62px;
    top: 500px;
    display: flex;
    align-items: center;
    gap: 22px;
  }
  .brand-mark {
    width: 26px;
    height: 26px;
    background: var(--ink);
  }
  .brand-name {
    font-size: 92px;
    line-height: 1;
    font-weight: 700;
    letter-spacing: 3px;
    text-transform: uppercase;
    color: var(--ink);
  }
  .base-band {
    position: absolute;
    left: 0;
    bottom: 0;
    width: 1200px;
    height: 40px;
    background: var(--band-dark);
  }
</style>
</head>
<body>
  <main class="business-card">
    <div class="hero-photo" role="img" aria-label="Black and white photograph of a barista's hand holding a cup beneath an espresso machine as coffee pours"></div>

    <address class="contact-block">
      <p class="contact-street">Shop 7b/118-120 Pelbourne Street</p>
      <p class="contact-suburb">East Dalvington 3981</p>
      <p class="contact-phone">Tel. 9462 3157</p>
      <p class="contact-web">www.talvemo.com.au</p>
    </address>

    <div class="brand">
      <span class="brand-mark"></span>
      <h1 class="brand-name">Talvemo</h1>
    </div>

    <div class="base-band"></div>
  </main>
</body>
</html>
```